Bottle label design for a mulberry brandy

Please create a label design for a mulberry brandy. The registered brand name is "Kolvat"
The brandy will be produced in Armenia from 100% mulberry.
Color of the product: transparent.
The product will be sold worldwide. The price will be between 30 and 50 USD. So the product will be in premium category.
Therefore we need a solid design, appropriate to the product price category. The design, however, needs to be modern and optimistic.
You can have mulberries on the label or not have, it is up to you.
We have chosen for the product some bottle types, the links to the available bottles you can find in the attachment. Ideally you show a picture of your label on the bottle you selected.

Target Market(s)

worldwide

```html
<!DOCTYPE html>
<html lang="en">
<head>
<meta charset="utf-8">
<title>Kolvat Mulberry Brandy Label</title>
<link rel="stylesheet" href="https://fonts.googleapis.com/css2?family=Cormorant+Garamond:wght@400;600&family=Parisienne&display=swap">
<style>
  :root {
    --canvas-bg: #f1f1f1;
    --label-paper: #ffffff;
    --label-ink: #1c1a1a;
    --text-dark: #2a2727;
    --text-light: #ffffff;
    --fruit-light: #f2f2f2;
    --fruit-mid: #9a9a9a;
  }
  * { margin: 0; padding: 0; box-sizing: border-box; }
  html, body {
    width: 848px;
    height: 1200px;
    overflow: hidden;
    background: var(--canvas-bg);
  }
  .canvas {
    position: relative;
    width: 848px;
    height: 1200px;
  }
  .label {
    position: absolute;
    left: 112px;
    top: 213px;
    width: 624px;
    height: 774px;
    background: var(--label-paper);
    overflow: hidden;
  }
  .label__field {
    position: absolute;
    inset: 0;
    width: 100%;
    height: 100%;
  }
  .label__brand {
    position: absolute;
    left: 206px;
    top: 92px;
    font-family: "Parisienne", cursive;
    font-size: 112px;
    line-height: 1;
    color: var(--text-dark);
    font-weight: 400;
    white-space: nowrap;
  }
  .label__tagline {
    position: absolute;
    left: 229px;
    top: 232px;
    font-family: "Cormorant Garamond", serif;
    font-size: 34px;
    line-height: 1;
    color: var(--text-dark);
    white-space: nowrap;
  }
  .label__tagline strong {
    font-weight: 600;
  }
  .label__fruit {
    position: absolute;
    left: 151px;
    top: 378px;
    width: 356px;
    height: 138px;
    border-radius: 20px;
    background: linear-gradient(135deg, var(--fruit-light) 0%, var(--fruit-mid) 100%);
  }
  .label__origin,
  .label__volume {
    position: absolute;
    font-family: "Cormorant Garamond", serif;
    font-size: 24px;
    line-height: 1;
    color: var(--text-light);
    white-space: nowrap;
  }
  .label__origin { left: 86px; top: 600px; }
  .label__volume { left: 181px; top: 648px; }
</style>
</head>
<body>
  <main class="canvas">
    <section class="label">
      <svg class="label__field" viewBox="0 0 624 774" preserveAspectRatio="none" aria-hidden="true">
        <polygon points="0,0 624,731 624,774 0,774" fill="var(--label-ink)"/>
      </svg>
      <h1 class="label__brand">Kolvat</h1>
      <p class="label__tagline">100% <strong>mulberry</strong> brandy</p>
      <div class="label__fruit" role="img" aria-label="Silhouette of two mulberries on a stem with a leaf"></div>
      <p class="label__origin">produced in Armenia</p>
      <p class="label__volume">700ml</p>
    </section>
  </main>
</body>
</html>
```